Bridal Pastry Trade Institute Website Homepage Revision

I need the "homepage" to the new Coastal Bridal Pastry Trade Institute to reworked. The current homepage is dull. It needs the attention of a professional graphic artist so it delivers a professionally finished feel and look. I have included the current URL for your viewing (builds.vornelt.com/coastal-pastry/cms/ ) to see where we are in the development phase. The elements on the homepage are all necessary and the colors are correct. I have also included the original Word document for the page (you can extract the RGB values and images from the doc). To be clear, I am not looking to recreate all the web pages, just the homepage. It needs to be responsive and stretched.

Target Market(s)

All bakers who sell wedding cakes in the United States

Number of Pages Required

1 page

Font styles to use
Other font styles liked:
• see the Word Document

Requirements
Must have
• It must have the elements already in the original mock up. That includes the colors and fonts.

```html
<!DOCTYPE html>
<html lang="en">
<head>
<meta charset="utf-8">
<title>Coastal Bridal Pastry Trade Institute — Home</title>
<link rel="stylesheet" href="https://fonts.googleapis.com/css2?family=Montserrat:wght@400;500;600&family=Kalam:wght@400&display=swap">
<style>
  :root {
    --pink: #ee2a7b;
    --teal: #00c4c6;
    --orange: #fa9300;
    --orange-dark: #d97d00;
    --white: #ffffff;
    --ink: #2b2b2b;
    --muted: #8a8a8a;
    --badge: #b9b9b9;
    --board: #e9ecef;
  }
  * { box-sizing: border-box; margin: 0; padding: 0; }
  html, body { width: 1200px; height: 819px; overflow: hidden; background: var(--white); }
  body { font-family: "Montserrat", Arial, sans-serif; color: var(--ink); position: relative; }

  .utility-bar {
    position: absolute; top: 0; left: 0; width: 1200px; height: 35px;
    background: var(--pink);
    display: flex; justify-content: flex-end; align-items: center;
    padding-right: 96px; gap: 30px;
  }
  .utility-bar a { color: var(--white); text-decoration: none; font-size: 11px; font-weight: 500; letter-spacing: .2px; }

  .main-nav {
    position: absolute; top: 35px; left: 0; width: 1200px; height: 78px;
    background: var(--white);
    display: flex; align-items: center; padding-left: 435px; gap: 26px;
  }
  .main-nav a { color: var(--ink); text-decoration: none; font-size: 11px; font-weight: 500; }
  .main-nav a.is-active { color: var(--pink); }

  .brand {
    position: absolute; top: 0; left: 92px; width: 325px; height: 184px;
    background: var(--white);
    box-shadow: 0 1px 4px rgba(0,0,0,.12);
    display: flex; align-items: center; justify-content: center; gap: 12px;
    padding: 0 22px; z-index: 2;
  }
  .brand-dot { width: 26px; height: 26px; border-radius: 50%; background: var(--pink); flex: none; }
  .brand-name { font-size: 19px; font-weight: 600; color: var(--pink); line-height: 1.25; }

  .hero {
    position: absolute; top: 113px; left: 0; width: 1200px; height: 536px;
    background: var(--teal);
  }
  .video-frame {
    position: absolute; top: 136px; left: 92px; width: 589px; height: 347px;
    border: 3px solid var(--white);
  }
  .video-still {
    position: absolute; inset: 0;
    background: linear-gradient(160deg, #f4f5f7 0%, var(--board) 60%, #dfe2e6 100%);
  }
  .video-play {
    position: absolute; top: 95px; left: 128px; width: 326px; height: 165px;
    background: var(--orange);
    display: flex; flex-direction: column; align-items: center; justify-content: center; gap: 14px;
    color: var(--white);
  }
  .video-play span { font-family: "Kalam", cursive; font-size: 27px; }

  .optin {
    position: absolute; top: 136px; left: 745px; width: 362px; height: 347px;
    border: 3px solid var(--white);
    padding: 26px 32px 0; text-align: center;
  }
  .optin h2 { color: var(--white); font-size: 20px; font-weight: 500; line-height: 1.3; }
  .optin hr { width: 44px; border: 0; border-top: 2px solid var(--white); margin: 16px auto 24px; }
  .optin .field {
    display: block; width: 292px; height: 41px; margin: 0 auto 15px;
    background: var(--white); border: 0; padding-left: 26px;
    font-family: "Montserrat", Arial, sans-serif; font-size: 11px; color: var(--muted);
    text-align: left; line-height: 41px;
  }
  .optin .submit {
    display: block; width: 292px; height: 43px; margin: 0 auto;
    background: var(--orange); border-bottom: 4px solid var(--orange-dark);
    color: var(--white); font-family: "Kalam", cursive; font-size: 16px; line-height: 40px;
  }

  .press {
    position: absolute; top: 649px; left: 0; width: 1200px; height: 170px;
    background: var(--white); text-align: center;
  }
  .press h3 { margin-top: 35px; font-size: 10px; font-weight: 500; color: var(--muted); letter-spacing: .4px; }
  .press-row { display: flex; justify-content: center; align-items: center; gap: 44px; margin-top: 30px; }
  .press-badge { background: var(--badge); }
</style>
</head>
<body>
  <nav class="utility-bar">
    <a href="#">BLOG</a>
    <a href="#">CONTACT</a>
    <a href="#">MEMBER LOGIN</a>
  </nav>

  <nav class="main-nav">
    <a href="#" class="is-active">HOME</a>
    <a href="#">RAY'S STORY</a>
    <a href="#">MARKETING SOLUTIONS</a>
    <a href="#">SALES SOLUTIONS</a>
    <a href="#">PARTNER WITH US</a>
    <a href="#">HIRE US</a>
  </nav>

  <div class="brand">
    <span class="brand-dot"></span>
    <span class="brand-name">Coastal Bridal Pastry Trade Institute</span>
  </div>

  <section class="hero">
    <div class="video-frame">
      <div class="video-still" role="img" aria-label="Whiteboard with handwritten notes about the Bridal Pastry Trade Institute sales method"></div>
      <div class="video-play">
        <svg width="40" height="40" viewBox="0 0 40 40" aria-hidden="true">
          <circle cx="20" cy="20" r="17.5" fill="none" stroke="#fff" stroke-width="2.5"/>
          <path d="M16 12 L28 20 L16 28 Z" fill="none" stroke="#fff" stroke-width="2.5" stroke-linejoin="round"/>
        </svg>
        <span>“Watch This First”</span>
      </div>
    </div>

    <form class="optin">
      <h2>How a New Discovery Sells More Wedding Cakes and at Higher Prices!</h2>
      <hr>
      <div class="field">Your First Name</div>
      <div class="field">Your email</div>
      <div class="submit">Watch Now!</div>
    </form>
  </section>

  <section class="press">
    <h3>RAY LINDELL AS SEEN ON</h3>
    <div class="press-row">
      <div class="press-badge" style="width:60px;height:40px;border-radius:4px"></div>
      <div class="press-badge" style="width:70px;height:52px"></div>
      <div class="press-badge" style="width:100px;height:44px;border-radius:4px"></div>
      <div class="press-badge" style="width:50px;height:50px;border-radius:50%"></div>
      <div class="press-badge" style="width:50px;height:48px;border-radius:4px"></div>
      <div class="press-badge" style="width:110px;height:38px;border-radius:4px"></div>
    </div>
  </section>
</body>
</html>
```